Cover for Where the Lantern Drifts Beyond the Quiet Shore

Cover for a book that describes everything that happens to a person, from pre-birth life plans through growing in compassion and wisdom to death and living in the afterlife. The information is revealed in messages from people living in the life after this life. The title is Patterns Behind the Seasons of Your Journey and Beyond: Told by Voices Dwelling Past the Veil. Author is T. Milton Baxby. Book size is 6 by 9.

Target Market(s)

General

Font styles to use
Serif

```html
<!DOCTYPE html>
<html lang="en">
<head>
<meta charset="utf-8">
<title>Patterns Behind the Seasons of Your Journey and Beyond — Cover</title>
<link rel="stylesheet" href="https://fonts.googleapis.com/css2?family=Amaranth:wght@400;700&family=Roboto:wght@300;400&family=Arimo&display=swap">
<style>
  :root {
    --backdrop: #1b1b1b;
    --ink: #1d5aa6;
    --ink-deep: #164a8f;
    --glow: rgba(255,255,255,0.95);
    --sky-top: #3f8fe0;
    --sky-mid: #9fd0f4;
    --cloud: #eef7fd;
    --blush: #f6e4ec;
  }
  * { margin: 0; padding: 0; box-sizing: border-box; }
  html, body { width: 1200px; height: 1085px; overflow: hidden; background: var(--backdrop); }
  .spread {
    position: absolute; left: 74px; top: 140px;
    width: 1047px; height: 773px; display: flex;
  }
  .back-cover, .spine, .front-cover { position: relative; height: 100%; overflow: hidden; }
  .back-cover { width: 502px; }
  .spine { width: 45px; }
  .front-cover { width: 500px; }

  .back-art {
    position: absolute; inset: 0;
    background:
      radial-gradient(ellipse 70% 45% at 40% 40%, rgba(255,255,255,0.85), transparent 70%),
      radial-gradient(ellipse 80% 40% at 50% 92%, rgba(150,200,240,0.6), transparent 70%),
      linear-gradient(180deg, #6cb4ee 0%, #bfe2f8 35%, var(--cloud) 60%, #a9d4f3 100%);
  }
  .spine-art {
    position: absolute; inset: 0;
    background: linear-gradient(180deg, #5aa8ea 0%, #d9eefb 45%, #eaf5fc 70%, #8cc4ef 100%);
  }
  .front-art {
    position: absolute; inset: 0;
    background:
      radial-gradient(ellipse 60% 30% at 45% 45%, rgba(255,255,255,0.9), transparent 70%),
      radial-gradient(ellipse 40% 25% at 85% 70%, var(--blush), transparent 70%),
      radial-gradient(ellipse 35% 28% at 40% 78%, rgba(90,140,200,0.45), transparent 70%),
      linear-gradient(180deg, var(--sky-top) 0%, #79bdf1 22%, var(--sky-mid) 40%, var(--cloud) 60%, #dbeefb 85%, #9ccbef 100%);
  }

  .blurb {
    position: absolute; left: 44px; top: 82px; width: 420px;
    font-family: "Arimo", Arial, sans-serif; font-size: 13.6px; line-height: 17.2px;
    color: var(--ink-deep); text-align: center;
  }
  .blurb p + p { margin-top: 17px; }

  .spine-text {
    position: absolute; left: 0; width: 45px;
    writing-mode: vertical-rl; display: flex; align-items: center;
    font-family: "Amaranth", sans-serif; color: var(--ink);
    text-shadow: 0 0 4px var(--glow);
    white-space: nowrap;
  }
  .spine-kicker { top: 28px; font-size: 11.5px; }
  .spine-title { top: 276px; font-size: 22px; }
  .spine-author { top: 612px; font-size: 19px; }

  .title-line, .subtitle-line, .author {
    position: absolute; left: 0; width: 100%; text-align: center;
    line-height: 1; color: var(--ink); white-space: nowrap;
    text-shadow: 0 0 6px var(--glow), 0 0 12px var(--glow);
  }
  .title-line { font-family: "Amaranth", sans-serif; }
  .title-xl { font-size: 66px; }
  .title-md { font-size: 44px; }
  .subtitle-line { font-family: "Roboto", sans-serif; font-weight: 300; font-size: 26px; }
  .author { font-family: "Amaranth", sans-serif; font-size: 38px; top: 686px; }
</style>
</head>
<body>
  <div class="spread">
    <section class="back-cover">
      <div class="back-art" role="img" aria-label="Soft blue sky with white clouds and a faint feather"></div>
      <div class="blurb">
        <p>Sed ultricies tellus a lobortis venenatis. Pellentesque vitae justo diam. Aliquam maximus tempus lobortis. Sed eu erat lacinia, pretium ante ut, ullamcorper ligula. Mauris interdum, risus vitae rhoncus feugiat, mi tellus fermentum ante, a ultrices mauris turpis vitae velit. Etiam vehicula malesuada orci, vehicula placerat tortor. Nam tincidunt egestas efficitur. Class aptent taciti sociosqu ad litora torquent per conubia nostra, per inceptos himenaeos. Morbi pretium gravida enim quis tristique. Suspendisse mi nulla, semper fringilla lobortis vel, pharetra at risus. Phasellus mauris elit, rhoncus nec fringilla nec, maximus at justo. In varius placerat turpis, eget porttitor ante condimentum in. Proin rutrum pharetra nisi in convallis. Vestibulum ornare massa quis metus lobortis mattis.</p>
        <p>Cras efficitur tempor leo, eget auctor nulla dignissim quis. Aliquam efficitur a est sed sollicitudin. Suspendisse sed ornare turpis, non accumsan neque. Praesent finibus risus id risus ultricies, eu imperdiet sem tempor. Donec semper consectetur dui, ac porta erat congue non.</p>
        <p>Donec nec sodales velit. Aliquam lacinia elit leo, dapibus elementum felis dignissim in. In volutpat egestas accumsan. Cras ac augue rutrum, lobortis justo sollicitudin, aliquet ipsum. Suspendisse potenti. Praesent et fermentum leo. Donec vehicula blandit neque eget pulvinar. Phasellus vel velit ut ligula imperdiet pretium quis et justo. Cras luctus nisi sapien, ac ultricies tortor elementum ut.</p>
      </div>
    </section>

    <section class="spine">
      <div class="spine-art" role="img" aria-label="Pale blue sky gradient"></div>
      <div class="spine-text spine-kicker">PATTERNS BEHIND THE SEASONS OF YOUR</div>
      <div class="spine-text spine-title">JOURNEY AND BEYOND</div>
      <div class="spine-text spine-author">T. MILTON BAXBY</div>
    </section>

    <section class="front-cover">
      <div class="front-art" role="img" aria-label="Starry blue sky with light rays, billowing white clouds and a large blue feather"></div>
      <h1>
        <span class="title-line title-xl" style="top:62px">PATTERNS</span>
        <span class="title-line title-md" style="top:134px">BEHIND THE SEASONS</span>
        <span class="title-line title-md" style="top:184px">OF YOUR</span>
        <span class="title-line title-xl" style="top:228px">JOURNEY</span>
        <span class="title-line title-md" style="top:294px">AND</span>
        <span class="title-line title-xl" style="top:340px">BEYOND:</span>
      </h1>
      <p>
        <span class="subtitle-line" style="top:416px">TOLD BY VOICES</span>
        <span class="subtitle-line" style="top:447px">DWELLING PAST</span>
        <span class="subtitle-line" style="top:477px">THE VEIL</span>
      </p>
      <p class="author">T. MILTON BAXBY</p>
    </section>
  </div>
</body>
</html>
```